Silver Falcon Construction Services

Create a business card for my business consulting company
Marissa Vendt, Founder and CEO
4816 Willow Crest Ave, Ste 310
Cedar Hollow, CO. 80999
720.555.0187 cell
mvendt@silverfalconbuild.example
www.silverfalconbuild.example

Target Market(s)

Private Equity and Construction Companies

Industry/Entity Type

Business / Sales Consulting

Tag Line that says "Where Every great venture is built one level at a time"

Requirements
Must have
• Logo on both sides of the card.
Nice to have
• Add tagline to the same side of the card as my name and contact info

```html
<!DOCTYPE html>
<html lang="en">
<head>
<meta charset="utf-8">
<title>Silver Falcon Construction Services – Business Card</title>
<link href="https://fonts.googleapis.com/css2?family=Montserrat:wght@500;700&family=Open+Sans:wght@400;600&family=Oswald:wght@600&display=swap" rel="stylesheet">
<style>
  :root {
    --ink: #111111;
    --paper: #ffffff;
    --stage: #3a3a3a;
    --muted: #555555;
    --rule: #c8c8c8;
    --haze: #ececec;
    --haze-dark: #222222;
  }
  * { box-sizing: border-box; margin: 0; padding: 0; }
  html, body { width: 1200px; height: 866px; overflow: hidden; }
  body {
    background: var(--stage);
    display: flex;
    align-items: center;
    justify-content: center;
    gap: 40px;
    font-family: "Open Sans", sans-serif;
  }
  .card {
    position: relative;
    width: 540px;
    height: 309px;
    overflow: hidden;
    box-shadow: 0 10px 26px rgba(0,0,0,.45);
  }

  /* Front */
  .card--front { background: var(--paper); color: var(--ink); }
  .front__haze, .back__haze {
    position: absolute; left: 0; top: 0; width: 320px; height: 240px;
  }
  .front__haze {
    background: radial-gradient(ellipse at 40% 20%, var(--haze) 0%, rgba(255,255,255,0) 70%);
  }
  .identity { position: absolute; left: 34px; top: 56px; width: 260px; }
  .identity__name {
    font-family: "Montserrat", sans-serif; font-weight: 700;
    font-size: 22px; letter-spacing: .5px; text-transform: uppercase;
  }
  .identity__title { font-size: 14px; color: var(--muted); margin-top: 1px; }
  .identity__rule { height: 1px; background: var(--rule); margin: 9px 0 8px; width: 240px; }
  .contact { list-style: none; font-size: 13px; line-height: 1.45; }
  .contact li { display: flex; align-items: center; gap: 8px; white-space: nowrap; }
  .contact svg { width: 12px; height: 12px; flex: none; fill: var(--ink); }

  .brand {
    position: absolute; right: 30px; top: 100px; width: 186px;
    display: flex; align-items: center; gap: 10px;
  }
  .brand__dot { width: 14px; height: 14px; border-radius: 50%; background: var(--ink); flex: none; }
  .brand__name {
    font-family: "Montserrat", sans-serif; font-weight: 700;
    font-size: 16px; line-height: 1.15; text-transform: uppercase; color: var(--ink);
  }

  .address__rule { position: absolute; right: 34px; bottom: 100px; width: 300px; height: 1px; background: var(--rule); }
  .address {
    position: absolute; right: 34px; bottom: 54px; text-align: right;
    font-style: normal; font-size: 13.5px; line-height: 1.35;
  }

  .band { position: absolute; left: 0; bottom: 0; width: 540px; height: 36px; }
  .tagline {
    position: absolute; right: 24px; bottom: 8px;
    font-family: "Oswald", sans-serif; font-weight: 600;
    font-size: 12px; letter-spacing: .3px; text-transform: uppercase; color: var(--paper);
    white-space: nowrap;
  }

  /* Back */
  .card--back { background: var(--ink); color: var(--paper); }
  .back__haze {
    background: radial-gradient(ellipse at 40% 20%, var(--haze-dark) 0%, rgba(17,17,17,0) 70%);
  }
  .card--back .brand {
    right: auto; left: 50%; top: 100px; transform: translateX(-50%); width: 250px;
  }
  .card--back .brand__dot { background: var(--paper); }
  .card--back .brand__name { color: var(--paper); font-size: 21px; }
  .back__web {
    position: absolute; left: 0; right: 0; bottom: 62px; text-align: center;
    font-size: 14px; letter-spacing: .6px;
  }
</style>
</head>
<body>

<section class="card card--front" aria-label="Card front">
  <div class="front__haze" role="img" aria-label="Faint mountain backdrop"></div>

  <div class="identity">
    <h1 class="identity__name">Marissa Vendt</h1>
    <p class="identity__title">Founder and CEO</p>
    <div class="identity__rule"></div>
    <ul class="contact">
      <li><svg viewBox="0 0 24 24"><path d="M6.6 10.8a15 15 0 0 0 6.6 6.6l2.2-2.2c.3-.3.7-.4 1-.2 1.1.4 2.3.6 3.6.6.6 0 1 .4 1 1V20c0 .6-.4 1-1 1C10.6 21 3 13.4 3 4c0-.6.4-1 1-1h3.5c.6 0 1 .4 1 1 0 1.3.2 2.5.6 3.6.1.3 0 .7-.2 1z"/></svg>720.555.0187</li>
      <li><svg viewBox="0 0 24 24"><path d="M2 5h20v14H2zm2 2v.5l8 5 8-5V7zm0 2.8V17h16V9.8l-8 5z"/></svg>mvendt@silverfalconbuild.example</li>
      <li><svg viewBox="0 0 24 24"><path d="M12 2a10 10 0 1 0 0 20 10 10 0 0 0 0-20zm6.9 9h-3a15 15 0 0 0-1.3-6.1A8 8 0 0 1 18.9 11zM12 4c1 1.4 1.8 4 1.9 7h-3.8C10.2 8 11 5.4 12 4zM9.4 4.9A15 15 0 0 0 8.1 11h-3a8 8 0 0 1 4.3-6.1zM5.1 13h3a15 15 0 0 0 1.3 6.1A8 8 0 0 1 5.1 13zM12 20c-1-1.4-1.8-4-1.9-7h3.8c-.1 3-.9 5.6-1.9 7zm2.6-.9a15 15 0 0 0 1.3-6.1h3a8 8 0 0 1-4.3 6.1z"/></svg>www.silverfalconbuild.example</li>
    </ul>
  </div>

  <div class="brand">
    <span class="brand__dot"></span>
    <span class="brand__name">Silver Falcon Construction Services</span>
  </div>

  <div class="address__rule"></div>
  <address class="address">
    4816 Willow Crest Ave,<br>Ste 310 Cedar Hollow, CO. 80999
  </address>

  <svg class="band" viewBox="0 0 540 36" preserveAspectRatio="none" aria-hidden="true">
    <path d="M0 30 H170 C182 30 182 8 196 8 H540 V36 H0 Z" fill="#111111"/>
  </svg>
  <p class="tagline">Every great venture is built one level at a time</p>
</section>

<section class="card card--back" aria-label="Card back">
  <div class="back__haze" role="img" aria-label="Faint mountain backdrop"></div>
  <div class="brand">
    <span class="brand__dot"></span>
    <span class="brand__name">Silver Falcon Construction Services</span>
  </div>
  <p class="back__web">www.silverfalconbuild.example</p>
</section>

</body>
</html>
```